Business card design for Velvet Harbor

We need business cards designed for our new marketing consulting company, Velvet Harbor. Our services include marketing strategy, go-to-market and launch planning, growth strategy, and execution. We serve medical technology and health technology companies, from startups to well-established growth companies.

The business cards should feel professional, credible, reliable and trustworthy, and should instill confidence. Also bold, creative, and modern.

The design must use the Velvet Harbor logo.

The primary brand color is this orange: #FF5501
A secondary color that you can use is this gray: #282B2D
I would prefer only to use the orange and gray. But if you feel you really need an additional accent color (please use it very sparingly, as little as possible), you can use this blue for small accent purposes: #009FED

Attached are the logo files. The main logo is the one with a little bit of orange on the left and the rest is gray.

The business card should include the following:

Velvet Harbor logo
First name and last name
Title
Email address
Phone number and type (in whatever order looks best for the design
Website (the website does not need to be in the same block as the personal info)

For example:

Nessa Pryle
Founder & Principal
nessa@velvetharbor.com
+1.628.309.4156 mobile (can use "." or spaces in between blocks of numbers)
velvetharbor.com (somewhere on the card, it does not need to be with the personal info; and note that there is no "www." at the beginning)

Note that there will be no address listed on the business card.

Target Market(s)

Executives (CEO, head of marketing, head of sales) at medical technology and health technology companies, mostly in their 40s and older, well-educated, often with advanced degrees. They are strategic thinkers, responsible for budgets, and familiar with P&L. Their comfort with and trust in using outside consultants varies.

Industry/Entity Type

Medical technology and health technology companies.

Contact Information for Business Card

See project description

Font styles to use
Sans Serif

Requirements
Must have
• Logo and see Business card details section above.

```html
<!DOCTYPE html>
<html lang="en">
<head>
<meta charset="utf-8">
<title>Velvet Harbor — Business Card</title>
<link rel="stylesheet" href="https://fonts.googleapis.com/css2?family=Arimo:wght@400;700&display=swap">
<style>
  :root {
    --brand-orange: #FF5501;
    --card-gray: #2d2e2f;
    --ink-white: #f4f4f4;
    --ink-soft: #d9d9d9;
    --divider: #8a8a8a;
    --backdrop: #e4e4e2;
  }
  * { box-sizing: border-box; margin: 0; padding: 0; }
  html, body { width: 1200px; height: 801px; overflow: hidden; }
  body {
    background: var(--backdrop);
    font-family: "Arimo", Arial, sans-serif;
    display: flex;
    align-items: center;
    justify-content: center;
    gap: 60px;
  }
  .card {
    position: relative;
    width: 525px;
    height: 300px;
    background: var(--card-gray);
    border-bottom: 4px solid var(--brand-orange);
    border-right: 2px solid var(--brand-orange);
    box-shadow: 0 10px 24px rgba(0,0,0,0.18);
    color: var(--ink-white);
  }
  /* Front */
  .brand-lockup {
    position: absolute;
    top: 58px;
    left: 0; right: 0;
    display: flex;
    align-items: center;
    justify-content: center;
    gap: 18px;
  }
  .brand-dot {
    width: 16px; height: 16px;
    border-radius: 50%;
    background: var(--brand-orange);
  }
  .brand-name {
    font-weight: 700;
    font-size: 26px;
    line-height: 1.05;
    letter-spacing: 0.34em;
    text-transform: uppercase;
    color: var(--ink-white);
  }
  .details {
    position: absolute;
    top: 176px;
    left: 0; right: 0;
    display: flex;
    justify-content: center;
    align-items: center;
    gap: 20px;
  }
  .person { text-align: right; }
  .person-name {
    color: var(--brand-orange);
    font-weight: 700;
    font-size: 21px;
  }
  .person-title {
    color: var(--ink-soft);
    font-size: 13.5px;
    margin-top: 4px;
  }
  .divider {
    width: 1px;
    height: 66px;
    background: var(--divider);
  }
  .contact-list { list-style: none; }
  .contact-list li {
    display: flex;
    align-items: center;
    gap: 9px;
    font-size: 13px;
    color: var(--ink-soft);
    line-height: 21px;
  }
  .contact-icon { width: 13px; height: 13px; flex: none; }
  /* Back */
  .back-wordmark {
    position: absolute;
    right: 34px;
    bottom: 62px;
    font-weight: 700;
    font-size: 34px;
    line-height: 1.08;
    letter-spacing: 0.34em;
    text-transform: uppercase;
    color: var(--ink-white);
    text-align: left;
  }
</style>
</head>
<body>
  <section class="card card-front" aria-label="Card front">
    <div class="brand-lockup">
      <span class="brand-dot"></span>
      <div class="brand-name">Velvet<br>Harbor</div>
    </div>
    <div class="details">
      <div class="person">
        <p class="person-name">Nessa Pryle</p>
        <p class="person-title">Founder &amp; Principal</p>
      </div>
      <span class="divider"></span>
      <ul class="contact-list">
        <li>
          <svg class="contact-icon" viewBox="0 0 24 24" aria-hidden="true"><path fill="#FF5501" d="M6.6 10.8a15.1 15.1 0 0 0 6.6 6.6l2.2-2.2c.3-.3.7-.4 1-.2 1.1.4 2.3.6 3.6.6.6 0 1 .4 1 1V20c0 .6-.4 1-1 1C10.6 21 3 13.4 3 4c0-.6.4-1 1-1h3.5c.6 0 1 .4 1 1 0 1.3.2 2.5.6 3.6.1.3 0 .7-.2 1z"/></svg>
          +1.628.309.4156
        </li>
        <li>
          <svg class="contact-icon" viewBox="0 0 24 24" aria-hidden="true"><rect x="2.5" y="5" width="19" height="14" rx="1.5" fill="none" stroke="#FF5501" stroke-width="2"/><path d="M3 6l9 7 9-7" fill="none" stroke="#FF5501" stroke-width="2"/></svg>
          nessa@velvetharbor.com
        </li>
        <li>
          <svg class="contact-icon" viewBox="0 0 24 24" aria-hidden="true"><g fill="none" stroke="#FF5501" stroke-width="2"><circle cx="12" cy="12" r="9.5"/><ellipse cx="12" cy="12" rx="4" ry="9.5"/><path d="M2.5 12h19M4 7h16M4 17h16"/></g></svg>
          velvetharbor.com
        </li>
      </ul>
    </div>
  </section>

  <section class="card card-back" aria-label="Card back">
    <div class="back-wordmark">Velvet<br>Harbor</div>
  </section>
</body>
</html>
```